UI/UX Design for AI Photo-to-Video Web Platform (Figma)

I am looking for a modern, high-converting redesign for my Next.js-based web platform. The service allows users to transform old photos into vibrant memories using AI. The design needs to be clean, intuitive, and "mobile-ready" (responsive).
Key Features to Visualize on the Homepage:
Photo Restoration & Colorization: A clear "before/after" visual showing a black-and-white photo turning into a high-quality color photo.
Photo-to-Video Animation: A visual representation of how both B&W and color photos are transformed into dynamic video clips.
Story Creation: A section showing how these photos and videos are combined into a single "Story Video" with background music.
Scope of Work:
Homepage Redesign: A hero section with the core value proposition and a visual walkthrough of the process.
Service/Internal Pages: Redesigning the functional pages where users upload files and manage their projects.
Responsive Design: While the focus is desktop, the layout must be designed with a "Mobile-First" mindset for easy porting to a mobile app later.
Technical Requirements for the Designer:
Tool: Must be designed in Figma.
Structure: Use Figma Auto Layout and Components for all elements (buttons, inputs, cards).
Design System: Provide a clear style guide (Typography, Color Palette, Spacing).
Assets: All icons should be in SVG format.
Style Preference:
Modern, sleek, and trustworthy.
Since the product is about "memories," the vibe should be emotional yet technologically advanced (AI-driven).

```html
<!DOCTYPE html>
<html lang="en">
<head>
<meta charset="utf-8">
<title>hueback.ai — Bring Your Old Memories Back to Life</title>
<link href="https://fonts.googleapis.com/css2?family=Figtree:wght@400;500;600;700&display=swap" rel="stylesheet">
<style>
:root{
  --bg:#ffffff;
  --ink:#1d1d26;
  --ink-soft:#3a3a45;
  --muted:#6b6b78;
  --line:#ececf1;
  --brand:#5a35e0;
  --brand-tint:#f5f2ff;
  --danger:#e0414b;
  --ok:#2e9a4f;
  --ok-tint:#e6f6ea;
  --shadow:0 6px 24px rgba(30,20,80,.08);
}
*{box-sizing:border-box;margin:0;padding:0}
html,body{width:1200px;height:2979px;overflow:hidden}
body{background:var(--bg);font-family:"Figtree",sans-serif;color:var(--ink);position:relative}
.abs{position:absolute}
svg{display:block}

.topbar{left:32px;top:18px;width:1135px;height:70px;border-radius:35px;background:#fff;box-shadow:var(--shadow);display:flex;align-items:center;padding:0 36px 0 40px}
.brand{font-size:27px;font-weight:600;letter-spacing:-.3px;color:var(--ink)}
.nav-links{display:flex;gap:6px;margin-left:44px;font-size:15.5px;color:var(--ink-soft)}
.nav-links a{padding:8px 14px;border-radius:18px;text-decoration:none;color:inherit}
.nav-links a.active{background:var(--brand-tint);font-weight:600;color:var(--ink)}
.credits{margin-left:auto;color:var(--brand);font-size:15.5px;font-weight:500}
.storage{margin-left:26px;font-size:15px;color:var(--ink-soft)}
.storage b{font-weight:600;color:var(--ink)}
.avatar{margin-left:24px;width:42px;height:42px;border-radius:50%;background:linear-gradient(135deg,#c9a48a,#6d4e3e)}

.hero-title{left:58px;top:192px;font-size:48px;line-height:54px;font-weight:700;letter-spacing:-.6px;width:520px}
.hero-title .accent{color:var(--brand)}
.hero-sub{left:58px;top:378px;width:500px;font-size:18.5px;line-height:26px;color:var(--ink-soft)}
.btn{display:inline-flex;align-items:center;justify-content:center;gap:9px;border-radius:26px;font-family:inherit;font-weight:500;border:0}
.btn-primary{background:var(--brand);color:#fff}
.btn-ghost{background:#fff;color:var(--ink);box-shadow:var(--shadow)}
.hero-cta{left:58px;top:462px;display:flex;gap:16px}
.hero-cta .btn{height:50px;font-size:17.5px;padding:0 30px}
.compare{left:603px;top:171px;width:535px;height:385px;border-radius:20px;overflow:hidden;box-shadow:var(--shadow)}
.compare .before{position:absolute;left:0;top:0;width:285px;height:100%;background:linear-gradient(160deg,#8d8d8d,#3d3d3d 60%,#222)}
.compare .after{position:absolute;left:285px;top:0;right:0;height:100%;background:linear-gradient(160deg,#6f7f4f,#2b3350 55%,#162038)}
.compare .divider{position:absolute;left:284px;top:0;width:3px;height:100%;background:#fff}
.compare .handle{position:absolute;left:263px;top:145px;width:46px;height:46px;border-radius:50%;background:#fff;display:flex;align-items:center;justify-content:center}

.tabs{left:57px;top:636px;display:flex;gap:17px}
.tab{height:50px;padding:0 28px;font-size:17.5px;border-radius:26px}
.disclaimer{left:990px;top:632px;width:148px;height:50px;font-size:14px;border-radius:26px}

.card{background:#fff;border-radius:26px;box-shadow:var(--shadow)}
.upload-card{left:58px;top:732px;width:1080px;height:437px}
.card-title{font-size:22px;font-weight:600}
.card-sub{font-size:15.5px;color:var(--ink-soft);margin-top:12px}
.dropzone{left:55px;top:125px;width:660px;height:253px;border:1.5px dashed #cfc6f5;border-radius:20px;background:#fbfaff;display:flex;flex-direction:column;align-items:center}
.drop-icon{width:48px;height:48px;border-radius:50%;background:#ece7ff;margin-top:38px;display:flex;align-items:center;justify-content:center}
.drop-title{font-size:15.5px;font-weight:600;margin-top:20px}
.drop-note{font-size:13.5px;color:var(--ink-soft);margin-top:16px}
.dropzone .btn{height:50px;padding:0 30px;font-size:17px;margin-top:18px}
.upload-visual{left:760px;top:55px;width:260px;height:320px;border-radius:20px;background:linear-gradient(150deg,#e9e6f3,#b9a99a 55%,#4a4f6a)}

.gallery-card{left:58px;top:1231px;width:1080px;height:1245px}
.toolbar{right:50px;top:48px;display:flex;gap:16px}
.tool{height:50px;background:#fff;box-shadow:var(--shadow);border-radius:25px;display:flex;align-items:center;justify-content:center}
.rule{left:55px;width:933px;height:1px;background:var(--line)}
.row-meta{left:52px;font-size:12.5px;color:var(--ink);display:flex;align-items:center}
.row-meta .id{color:var(--brand)}
.pill{background:var(--ok-tint);color:var(--ok);font-size:11.5px;padding:2px 12px;border-radius:10px;margin-left:8px}
.thumbs{left:53px;display:flex;gap:12px}
.thumb{width:247px;height:213px;border-radius:12px}
.thumb.bw{background:linear-gradient(150deg,#9a9a9a,#4a4a4a 65%,#2b2b2b)}
.actions{left:838px;display:flex;flex-direction:column;gap:19px}
.actions .btn{width:192px;height:49px;font-size:17.5px}
.btn-danger{background:#fff;color:var(--danger);box-shadow:var(--shadow)}
.load-more{left:465px;top:1106px;height:49px;width:155px;font-size:17px}
.end-note{left:0;width:100%;top:1177px;text-align:center;font-size:13.5px;color:var(--ink-soft)}

.footer{left:58px;top:2550px;width:1080px;height:390px}
.foot-brand{left:54px;top:50px}
.foot-brand .brand{font-size:27px}
.foot-brand p{margin-top:22px;font-size:15.5px;line-height:24px;color:var(--ink-soft);width:300px}
.foot-col{top:48px;width:160px}
.foot-col h4{font-size:18.5px;font-weight:600;margin-bottom:16px}
.foot-col a{display:block;font-size:15.5px;line-height:30px;color:var(--ink-soft);text-decoration:none}
.foot-rule{left:38px;top:328px;width:1005px;height:1px;background:var(--line)}
.copyright{left:0;width:100%;top:354px;text-align:center;font-size:13.5px;color:var(--ink-soft)}
</style>
</head>
<body>

<header class="topbar abs">
  <span class="brand">hueback.ai</span>
  <nav class="nav-links">
    <a class="active" href="#">Home</a><a href="#">How It Works</a><a href="#">Examples</a><a href="#">Pricing</a><a href="#">Studio</a><a href="#">Mara Tenn</a>
  </nav>
  <span class="credits">4740 credits</span>
  <span class="storage"><b>114 MB</b> / 1.0GB</span>
  <div class="avatar" role="img" aria-label="User profile photo"></div>
</header>

<h1 class="hero-title abs">Bring Your Old Memories Back to Life <span class="accent">with AI Magic</span></h1>
<p class="hero-sub abs">Restore, colorize, animate, and turn your old photos into cinematic videos — all in seconds.</p>
<div class="hero-cta abs">
  <span class="btn btn-primary"><svg width="20" height="20" viewBox="0 0 24 24" fill="none" stroke="#fff" stroke-width="1.8"><rect x="3" y="3" width="18" height="18" rx="4"/><circle cx="9" cy="9" r="2"/><path d="M21 15l-5-5-9 11"/></svg>Upload Photos</span>
  <span class="btn btn-ghost">See How It Works</span>
</div>
<div class="compare abs">
  <div class="before" role="img" aria-label="Black and white family portrait before restoration"></div>
  <div class="after" role="img" aria-label="Same family portrait restored in full color"></div>
  <div class="divider"></div>
  <div class="handle"><svg width="26" height="26" viewBox="0 0 24 24" fill="none" stroke="#444" stroke-width="1.8" stroke-linecap="round"><path d="M12 3v18M3 12h18M9 6l3-3 3 3M9 18l3 3 3-3M6 9l-3 3 3 3M18 9l3 3-3 3"/></svg></div>
</div>

<div class="tabs abs">
  <span class="btn btn-primary tab"><svg width="20" height="20" viewBox="0 0 24 24" fill="none" stroke="#fff" stroke-width="1.8"><rect x="3" y="3" width="18" height="18" rx="4"/><circle cx="9" cy="9" r="2"/><path d="M21 15l-5-5-9 11"/></svg>Images</span>
  <span class="btn btn-ghost tab"><svg width="22" height="20" viewBox="0 0 24 22" fill="none" stroke="#222" stroke-width="1.7"><rect x="2" y="4" width="20" height="15" rx="2"/><path d="M2 8h20M7 4l-2 4M12 4l-2 4M17 4l-2 4"/></svg>Video animations</span>
  <span class="btn btn-ghost tab"><svg width="20" height="22" viewBox="0 0 20 22" fill="none" stroke="#222" stroke-width="1.6"><rect x="6" y="2" width="8" height="12" rx="4"/><path d="M3 10a7 7 0 0 0 14 0M10 17v4"/></svg>Studio</span>
</div>
<span class="btn btn-ghost disclaimer abs"><svg width="18" height="18" viewBox="0 0 24 24" fill="none" stroke="#222" stroke-width="1.8"><circle cx="12" cy="12" r="9"/><path d="M12 11v6M12 7.5v.5"/></svg>AI Disclaimer</span>

<section class="card upload-card abs">
  <div class="abs" style="left:55px;top:44px">
    <h2 class="card-title">Upload Images</h2>
    <p class="card-sub">Upload photos to generate vintage and real color versions.</p>
  </div>
  <div class="dropzone abs">
    <div class="drop-icon"><svg width="26" height="26" viewBox="0 0 24 24" fill="none" stroke="var(--brand)" stroke-width="1.8" stroke-linecap="round"><path d="M7 18a4.5 4.5 0 0 1-.5-9A6 6 0 0 1 18 9a4 4 0 0 1 0 9"/><path d="M12 20v-8M9 14l3-3 3 3"/></svg></div>
    <div class="drop-title">Drag &amp; drop your images here</div>
    <div class="drop-note">Maximum 20 images -100MB total - JP, PNG, GIF, TIFF up to 10MB each</div>
    <span class="btn btn-primary"><svg width="20" height="18" viewBox="0 0 24 20" fill="none" stroke="#fff" stroke-width="1.8"><path d="M2 4a2 2 0 0 1 2-2h5l2 3h9a2 2 0 0 1 2 2v9a2 2 0 0 1-2 2H4a2 2 0 0 1-2-2z"/></svg>Select Files</span>
  </div>
  <div class="upload-visual abs" role="img" aria-label="Illustration of a black and white photo becoming a color photo"></div>
</section>

<section class="card gallery-card abs">
  <div class="abs" style="left:55px;top:42px">
    <h2 class="card-title">Images</h2>
    <p class="card-sub">Each row shows Origninal, Vintage Color, and Real Color.</p>
  </div>
  <div class="toolbar abs">
    <span class="tool" style="width:162px;gap:12px;font-size:17.5px"><svg width="22" height="18" viewBox="0 0 22 18" stroke="#222" stroke-width="1.8" stroke-linecap="round"><path d="M2 3h18M5 9h12M8 15h6"/></svg>Filter<svg width="14" height="10" viewBox="0 0 14 10" fill="none" stroke="#222" stroke-width="1.8"><path d="M2 3l5 5 5-5"/></svg></span>
    <span class="tool" style="width:50px"><svg width="22" height="22" viewBox="0 0 22 22" fill="none" stroke="#222" stroke-width="1.6"><rect x="2" y="2" width="7" height="7" rx="1.5"/><rect x="13" y="2" width="7" height="7" rx="1.5"/><rect x="2" y="13" width="7" height="7" rx="1.5"/><rect x="13" y="13" width="7" height="7" rx="1.5"/></svg></span>
    <span class="tool" style="width:50px"><svg width="22" height="18" viewBox="0 0 22 18" stroke="#222" stroke-width="1.8" stroke-linecap="round"><path d="M7 3h13M7 9h13M7 15h13M2 3h.5M2 9h.5M2 15h.5"/></svg></span>
  </div>

  <div class="rule abs" style="top:140px"></div>
  <div class="row-meta abs" style="top:177px"><span>Original ID:&nbsp;</span><span class="id">OL09YDYS</span>&nbsp;May 12,2025 - 10.24 AM<span style="margin-left:16px">Vintage</span><span class="pill">Done</span><span style="margin-left:150px">Real</span><span class="pill">Done</span></div>
  <div class="thumbs abs" style="top:208px">
    <div class="thumb bw" role="img" aria-label="Original black and white photo of a man in a hat beside a car"></div>
    <div class="thumb" style="background:linear-gradient(150deg,#6f8a55,#2f3f73 55%,#1c2233)" role="img" aria-label="Vintage color version of the man in a hat"></div>
    <div class="thumb" style="background:linear-gradient(150deg,#7a9460,#2b3e7a 55%,#1a2030)" role="img" aria-label="Real color version of the man in a hat"></div>
  </div>
  <div class="actions abs" style="top:212px">
    <span class="btn btn-ghost"><svg width="22" height="22" viewBox="0 0 24 24" fill="none" stroke="#222" stroke-width="1.7"><path d="M4 12a8 8 0 1 0 2.5-5.8M4 4v4h4"/><circle cx="12" cy="12" r="3"/></svg>Rotate</span>
    <span class="btn btn-danger"><svg width="20" height="22" viewBox="0 0 20 22" fill="none" stroke="var(--danger)" stroke-width="1.7"><path d="M2 5h16M7 5V3h6v2M4 5l1 15h10l1-15M8 9v8M12 9v8"/></svg>Delete</span>
    <span class="btn btn-primary"><svg width="22" height="22" viewBox="0 0 24 24" fill="none" stroke="#fff" stroke-width="1.7"><circle cx="11" cy="13" r="8"/><path d="M11 9v8M7 13h8M19 2v4M17 4h4"/></svg>Generate (20)</span>
  </div>

  <div class="rule abs" style="top:463px"></div>
  <div class="row-meta abs" style="top:500px;left:55px"><span>Original ID:&nbsp;</span><span class="id">OL09YDYS</span>&nbsp;May 12,2025 - 10.24 AM<span style="margin-left:16px">Vintage</span><span class="pill">Done</span><span style="margin-left:140px">Real</span><span class="pill">Done</span></div>
  <div class="thumbs abs" style="top:531px;left:55px">
    <div class="thumb bw" role="img" aria-label="Original black and white photo of a young man and a girl"></div>
    <div class="thumb" style="background:linear-gradient(150deg,#c9b99a,#3b3f52 55%,#cfc6b0)" role="img" aria-label="Vintage color version of the young man and girl"></div>
    <div class="thumb" style="background:linear-gradient(150deg,#d2c3a3,#34384d 55%,#d8d0bd)" role="img" aria-label="Real color version of the young man and girl"></div>
  </div>
  <div class="actions abs" style="top:527px;left:840px">
    <span class="btn btn-ghost"><svg width="22" height="22" viewBox="0 0 24 24" fill="none" stroke="#222" stroke-width="1.7"><path d="M4 12a8 8 0 1 0 2.5-5.8M4 4v4h4"/><circle cx="12" cy="12" r="3"/></svg>Rotate</span>
    <span class="btn btn-danger"><svg width="20" height="22" viewBox="0 0 20 22" fill="none" stroke="var(--danger)" stroke-width="1.7"><path d="M2 5h16M7 5V3h6v2M4 5l1 15h10l1-15M8 9v8M12 9v8"/></svg>Delete</span>
    <span class="btn btn-primary"><svg width="22" height="22" viewBox="0 0 24 24" fill="none" stroke="#fff" stroke-width="1.7"><circle cx="11" cy="13" r="8"/><path d="M11 9v8M7 13h8M19 2v4M17 4h4"/></svg>Generate (20)</span>
  </div>

  <div class="rule abs" style="top:780px"></div>
  <div class="row-meta abs" style="top:817px"><span>Original ID:&nbsp;</span><span class="id">OL09YDYS</span>&nbsp;May 12,2025 - 10.24 AM<span style="margin-left:16px">Vintage</span><span class="pill">Done</span><span style="margin-left:150px">Real</span><span class="pill">Done</span></div>
  <div class="thumbs abs" style="top:848px">
    <div class="thumb bw" role="img" aria-label="Original black and white family portrait"></div>
    <div class="thumb" style="background:linear-gradient(150deg,#6f7f4f,#2b3350 55%,#162038)" role="img" aria-label="Vintage color version of the family portrait"></div>
    <div class="thumb" style="background:linear-gradient(150deg,#7b8c58,#27304e 55%,#141c33)" role="img" aria-label="Real color version of the family portrait"></div>
  </div>
  <div class="actions abs" style="top:845px;left:839px">
    <span class="btn btn-ghost"><svg width="22" height="22" viewBox="0 0 24 24" fill="none" stroke="#222" stroke-width="1.7"><path d="M4 12a8 8 0 1 0 2.5-5.8M4 4v4h4"/><circle cx="12" cy="12" r="3"/></svg>Rotate</span>
    <span class="btn btn-danger"><svg width="20" height="22" viewBox="0 0 20 22" fill="none" stroke="var(--danger)" stroke-width="1.7"><path d="M2 5h16M7 5V3h6v2M4 5l1 15h10l1-15M8 9v8M12 9v8"/></svg>Delete</span>
    <span class="btn btn-primary"><svg width="22" height="22" viewBox="0 0 24 24" fill="none" stroke="#fff" stroke-width="1.7"><circle cx="11" cy="13" r="8"/><path d="M11 9v8M7 13h8M19 2v4M17 4h4"/></svg>Generate (20)</span>
  </div>

  <span class="btn btn-primary load-more abs">Load More</span>
  <p class="end-note abs">Your're reached the end of your results.</p>
</section>

<footer class="card footer abs">
  <div class="foot-brand abs">
    <span class="brand">hueback.ai</span>
    <p>Bring Your Memories Back to Life Transform your old photos into cinematic stories with AI.</p>
  </div>
  <div class="foot-col abs" style="left:397px"><h4>Resources</h4><a href="#">Blog</a><a href="#">Help Center</a><a href="#">Tutorials</a><a href="#">API (optional<br>future)</a><a href="#">Status</a></div>
  <div class="foot-col abs" style="left:569px"><h4>Company</h4><a href="#">About Us</a><a href="#">Careers</a><a href="#">Contact</a><a href="#">Press</a><a href="#">Affiliates</a></div>
  <div class="foot-col abs" style="left:741px"><h4>Product</h4><a href="#">How It Works</a><a href="#">Features</a><a href="#">Pricing</a><a href="#">Examples</a><a href="#">AI Studio</a></div>
  <div class="foot-col abs" style="left:913px"><h4>Legal</h4><a href="#">Privacy Policy</a><a href="#">Terms of Service</a><a href="#">Cookie Policy</a><a href="#">AI Disclaimer</a></div>
  <div class="foot-rule abs"></div>
  <p class="copyright abs">© 2026 HueBack AI. All rights reserved.</p>
</footer>

</body>
</html>
```